Quick 1hr job to create exciting page header & footer designs

We need some exciting and engaging header and footer designs for school yearbooks, in particular for the NZ Primary school market (children 5 to 10 years old).
The header and footer designs need to be bright and colourful, and should appeal to younger children. Header and footer graphics do not need to be the same, but should at least relate to each other thematically.
Please include the following sample text on the header: Sports Day.
Please include this sample text on the footer: Primary School Name 2014.
Note that the header/footers may be used without the text so the design should work with or without the text. Header/footer may be used over top of a coloured or graphic background. The graphic could be illustrative, photographic or patterned, the more creative the better.

Header dimensions: 198.88 mm w x 15.24 mm h
Footer dimensions: 198.88 mm w x 6.35 mm h

Please see the example pages provided, but please note we are looking for something more suitable for Primary Schools, and a lot more dynamic and interesting!

Target Market(s)

New Zealand Primary Schools

Industry/Entity Type

School

Requirements
Must have
• Must contain sample text and must be suitable for younger children
• Must be appropriate for the New Zealand market, i.e. don't use imagery that is obviously from other countries.

```html
<!DOCTYPE html>
<html lang="en">
<head>
<meta charset="utf-8">
<title>Sports Day – Yearbook Header &amp; Footer</title>
<link href="https://fonts.googleapis.com/css2?family=Arimo:wght@700&family=Archivo+Black&display=swap" rel="stylesheet">
<style>
  :root {
    --page: #ffffff;
    --band-edge: #0b8fd6;
    --band-mid: #86ccf0;
    --gold-top: #ffe14a;
    --gold-bottom: #f08a12;
    --magenta: #e0177f;
    --yellow: #ffe600;
    --orange: #ea7a1a;
    --purple: #8b1e7e;
    --green: #8cc63f;
    --white: #ffffff;
    --ink-blue: #1a6fd1;
    --shadow: rgba(60, 30, 0, .55);
  }
  * { margin: 0; padding: 0; box-sizing: border-box; }
  html, body { width: 1200px; height: 538px; overflow: hidden; background: var(--page); }
  .page { position: relative; width: 1200px; height: 538px; background: var(--page); overflow: hidden; }

  .band {
    position: absolute; left: 0; width: 1200px;
    background: linear-gradient(90deg, var(--band-edge) 0%, var(--band-mid) 45%, var(--band-mid) 55%, var(--band-edge) 100%);
  }
  .header-band { top: 124px; height: 88px; }
  .footer-band { top: 437px; height: 35px; }

  .puzzle-art { position: absolute; }
  .puzzle-art--header-left {
    left: 0; top: 124px; width: 370px; height: 88px;
    background: linear-gradient(90deg, var(--magenta) 0%, var(--purple) 30%, var(--green) 60%, var(--yellow) 100%);
    -webkit-mask-image: linear-gradient(90deg, #000 55%, transparent 100%);
    mask-image: linear-gradient(90deg, #000 55%, transparent 100%);
  }
  .puzzle-art--header-right {
    left: 1020px; top: 124px; width: 180px; height: 88px;
    background: linear-gradient(90deg, var(--orange), var(--orange));
    -webkit-mask-image: linear-gradient(90deg, transparent 0%, #000 45%, #000 80%, transparent 100%);
    mask-image: linear-gradient(90deg, transparent 0%, #000 45%, #000 80%, transparent 100%);
  }
  .puzzle-art--footer-left {
    left: 0; top: 437px; width: 300px; height: 35px;
    background: linear-gradient(90deg, var(--purple) 0%, var(--green) 40%, var(--yellow) 70%, var(--orange) 100%);
    -webkit-mask-image: linear-gradient(90deg, #000 55%, transparent 100%);
    mask-image: linear-gradient(90deg, #000 55%, transparent 100%);
  }

  .header-title {
    position: absolute; left: 440px; top: 128px;
    font-family: "Arimo", Arial, sans-serif; font-weight: 700;
    font-size: 78px; line-height: 1; letter-spacing: -1px;
    background: linear-gradient(180deg, var(--gold-top) 20%, var(--gold-bottom) 85%);
    -webkit-background-clip: text; background-clip: text; color: transparent;
    filter: drop-shadow(3px 3px 0 var(--shadow));
  }

  .letter-tile {
    position: absolute; width: 66px; height: 66px;
    display: flex; align-items: center; justify-content: center;
    font-family: "Arimo", Arial, sans-serif; font-weight: 700; font-size: 32px;
    box-shadow: 2px 3px 3px rgba(0,0,0,.35);
  }
  .letter-tile--d { left: 722px; top: 134px; background: var(--magenta); color: var(--white); transform: rotate(-12deg); }
  .letter-tile--a { left: 818px; top: 142px; background: var(--yellow); color: var(--orange); transform: rotate(4deg); }
  .letter-tile--y { left: 922px; top: 134px; background: var(--white); color: var(--ink-blue); transform: rotate(18deg); }

  .footer-title {
    position: absolute; left: 366px; top: 437px;
    font-family: "Archivo Black", Arial, sans-serif;
    font-size: 32px; line-height: 35px; letter-spacing: 11px;
    background: linear-gradient(180deg, var(--gold-top) 20%, var(--gold-bottom) 85%);
    -webkit-background-clip: text; background-clip: text; color: transparent;
    filter: drop-shadow(1px 1px 0 var(--shadow));
    white-space: nowrap;
  }
</style>
</head>
<body>
  <main class="page">
    <header class="yearbook-header">
      <div class="band header-band"></div>
      <div class="puzzle-art puzzle-art--header-left" role="img" aria-label="Cluster of colourful jigsaw puzzle pieces"></div>
      <div class="puzzle-art puzzle-art--header-right" role="img" aria-label="Orange jigsaw puzzle piece"></div>
      <h1 class="header-title">Sports</h1>
      <span class="letter-tile letter-tile--d">D</span>
      <span class="letter-tile letter-tile--a">a</span>
      <span class="letter-tile letter-tile--y">y</span>
    </header>
    <footer class="yearbook-footer">
      <div class="band footer-band"></div>
      <div class="puzzle-art puzzle-art--footer-left" role="img" aria-label="Small cluster of colourful jigsaw puzzle pieces"></div>
      <p class="footer-title">Primary School Name 2014</p>
    </footer>
  </main>
</body>
</html>
```